731 Orchard Avenue Residences

designing a sign for apartment complex;
prefer colors gray white and yellow

Target Market(s)

residents coming home to their apartment

Font styles to use
Serif
Sans Serif

Colors
FFF300
FFF600
FEFA6F
FFFEC7
FFFEE8

Requirements
Must have
• black or gray, white and some yellow; easy to read and see

```html
<!DOCTYPE html>
<html lang="en">
<head>
<meta charset="utf-8">
<title>731 Orchard Avenue Residences — Sign</title>
<link rel="stylesheet" href="https://fonts.googleapis.com/css2?family=Anton&family=Arimo:wght@700&display=swap">
<style>
  :root {
    --backdrop: #080908;
    --slate: #333333;
    --signal-yellow: #f2fc14;
    --white: #ffffff;
  }
  html, body {
    margin: 0;
    padding: 0;
    overflow: hidden;
    background: var(--backdrop);
  }
  .canvas {
    position: relative;
    width: 927px;
    height: 1200px;
    background: var(--backdrop);
    overflow: hidden;
  }
  .sign {
    position: absolute;
    display: block;
  }
  .sign--landscape { left: 144px; top: 141px; width: 367px; height: 283px; }
  .sign--portrait  { left: 416px; top: 564px; width: 380px; height: 493px; }

  .fill-slate  { fill: var(--slate); }
  .fill-yellow { fill: var(--signal-yellow); }
  .fill-white  { fill: var(--white); }

  .street-number {
    font-family: "Anton", "Oswald", sans-serif;
    fill: var(--signal-yellow);
  }
  .street-name {
    font-family: "Anton", "Oswald", sans-serif;
    fill: var(--slate);
  }
  .residences-label {
    font-family: "Arimo", Arial, sans-serif;
    font-weight: 700;
    fill: var(--slate);
  }
</style>
</head>
<body>
<main class="canvas">

  <!-- Landscape wall sign -->
  <svg class="sign sign--landscape" viewBox="0 0 669 516" aria-labelledby="sign-a-title">
    <title id="sign-a-title">731 Orchard Avenue Residences</title>
    <rect class="panel-top fill-slate" x="0" y="0" width="669" height="241"/>
    <g class="mount-bracket fill-white">
      <rect x="481" y="43" width="46" height="44"/>
      <rect x="526" y="56" width="143" height="17"/>
    </g>
    <text class="street-number" x="74" y="240" font-size="152" textLength="218" lengthAdjust="spacingAndGlyphs">731</text>
    <rect class="panel-middle fill-yellow" x="0" y="240" width="669" height="171"/>
    <rect class="emblem-area fill-yellow" x="385" y="157" width="244" height="84" role="img" aria-label="House roofline emblem"/>
    <text class="street-name" x="63" y="356" font-size="86" textLength="544" lengthAdjust="spacingAndGlyphs">ORCHARD AVENUE</text>
    <rect class="label-strip fill-white" x="0" y="410" width="669" height="106"/>
    <text class="residences-label" x="60" y="474" font-size="47" textLength="552" lengthAdjust="spacing">RESIDENCES</text>
  </svg>

  <!-- Portrait post sign -->
  <svg class="sign sign--portrait" viewBox="0 0 693 898" aria-labelledby="sign-b-title">
    <title id="sign-b-title">731 Orchard Avenue Residences</title>
    <rect class="panel-top fill-slate" x="0" y="0" width="693" height="345"/>
    <g class="mount-bracket fill-white">
      <rect x="367" y="65" width="61" height="58"/>
      <rect x="427" y="82" width="266" height="24"/>
    </g>
    <text class="street-number" x="76" y="344" font-size="160" textLength="225" lengthAdjust="spacingAndGlyphs">731</text>
    <rect class="panel-lower fill-yellow" x="0" y="344" width="693" height="554"/>
    <rect class="emblem-area fill-yellow" x="399" y="258" width="254" height="87" role="img" aria-label="House roofline emblem"/>
    <text class="street-name" x="64" y="489" font-size="89" textLength="564" lengthAdjust="spacingAndGlyphs">ORCHARD AVENUE</text>
    <rect class="label-strip fill-white" x="0" y="565" width="693" height="110"/>
    <text class="residences-label" x="61" y="634" font-size="45" textLength="572" lengthAdjust="spacing">RESIDENCES</text>
    <g class="mount-bracket fill-slate">
      <rect x="0" y="808" width="188" height="24"/>
      <rect x="187" y="791" width="61" height="58"/>
    </g>
  </svg>

</main>
</body>
</html>
```